Fundraiser Flyer and Email Template

We are looking for a flexible coordinated flyer and email template. The feel of both should be more formal or professional. We are not looking for an overly "political" design that features American flags or other "political" symbols.

We are a political fundraising firm that works with elected officials to set up fundraisers for their campaigns. We send the invites to these events via US Mail and email, so we are looking for a standardized template that will work as both an 8.5 x 11 inch printed flyer, as well as an email template.

The information in the email will be text, but images can be used for formatting.

Some clients have a campaign logo, others do not. The format should be flexible enough to either include the logo, or leave it out. Size also varies.

Any colors in the template should be editable so we can match logos as we get them.

We're open to any format that allows us to edit the format as needed. This would include Photoshop, Microsoft Word, etc.

The text of the invite should include space for:

---------------------------------------
NAME
DISTRICT NUMBER AND OFFICE

DATE OF EVENT
TIME OF EVENT

LOCATION
LOCATION ADDRESS
LOCATION CITY, STATE, ZIP

SUGGESTED CONTRIBUTION LEVELS (Typically 3 levels are provided such as Gold: $1,000, Silver: $500, Bronze: $250)

ADDRESS TO SEND CHECKS TO

RSVP CONTACT INFORMATION

The invite will also need fine-print at the bottom that reads:
"Pennsylvania law allows personal, partnership, and PAC contributions. By law we cannot accept corporate contributions
Paid for by [NAME]"

It Professional

Serif
Sans Serif

• Must have spaces for:
• NAME
• DISTRICT NUMBER AND OFFICE
• DATE OF EVENT
• TIME OF EVENT
• LOCATION
• LOCATION ADDRESS
• LOCATION CITY, STATE, ZIP
• SUGGESTED CONTRIBUTION LEVELS (Typically 3 levels are provided such as Gold: $1,000, Silver: $500, Bronze: $250)
• ADDRESS TO SEND CHECKS TO
• RSVP CONTACT INFORMATION
• The invite will also need fine-print at the bottom that reads:
• "Pennsylvania law allows personal, partnership, and PAC contributions. By law we cannot accept corporate contributions
• Paid for by [NAME]"
• It should not be overly "political".

```html
<!DOCTYPE html>
<html lang="en">
<head>
<meta charset="utf-8">
<title>Marcus Whitfield – Annual Fundraiser Invitation</title>
<link href="https://fonts.googleapis.com/css2?family=Montserrat:wght@400;500;600;700;800;900&display=swap" rel="stylesheet">
<style>
  :root {
    --blue-deep: #1b2f8f;
    --blue-mid: #1f4fc0;
    --blue-bright: #2a63d6;
    --red: #e3121f;
    --red-dark: #c50d18;
    --white: #ffffff;
    --ink: #111111;
    --muted: #3a3a3a;
    --line: #222222;
  }
  * { box-sizing: border-box; margin: 0; padding: 0; }
  html, body { width: 993px; height: 1200px; overflow: hidden; background: #eeeae4; }
  body { font-family: "Montserrat", Arial, sans-serif; color: var(--ink); }

  .flyer {
    position: relative;
    width: 993px;
    height: 1200px;
    overflow: hidden;
    background:
      radial-gradient(ellipse at 20% 30%, rgba(70,130,240,.55), transparent 55%),
      radial-gradient(ellipse at 85% 90%, rgba(60,110,220,.45), transparent 50%),
      linear-gradient(150deg, var(--blue-mid) 0%, var(--blue-bright) 35%, var(--blue-deep) 100%);
  }

  .candidate-first {
    position: absolute;
    left: 350px;
    top: 120px;
    font-size: 84px;
    font-weight: 900;
    letter-spacing: 1px;
    color: var(--white);
    line-height: 1;
  }

  .content-panel {
    position: absolute;
    left: 290px;
    top: 210px;
    width: 663px;
    height: 740px;
    background: var(--white);
    border-radius: 0 0 22px 22px;
  }

  .portrait {
    position: absolute;
    left: 40px;
    top: 200px;
    width: 300px;
    height: 250px;
    border-radius: 22px;
    border: 5px solid var(--white);
    background: radial-gradient(ellipse at 50% 60%, #5a5a5e 0%, #2a2a2d 55%, #121214 100%);
    box-shadow: 0 6px 16px rgba(0,0,0,.35);
    z-index: 2;
  }

  .panel-inner { position: absolute; left: 60px; top: 10px; right: 30px; }

  .candidate-last {
    font-size: 84px;
    font-weight: 900;
    color: var(--red);
    line-height: 1;
    letter-spacing: 1px;
  }
  .district {
    margin-top: 12px;
    font-size: 16px;
    font-weight: 500;
    letter-spacing: .5px;
    text-transform: uppercase;
  }
  .invite-line {
    margin-top: 14px;
    font-size: 24px;
    font-weight: 700;
  }

  .date-band {
    position: absolute;
    left: 340px;
    top: 410px;
    width: 613px;
    height: 118px;
    background: linear-gradient(90deg, var(--red) 0%, var(--red-dark) 100%);
    border-radius: 22px 0 0 22px;
    color: var(--white);
    padding: 20px 0 0 36px;
    font-weight: 800;
    font-size: 32px;
    line-height: 1.25;
    text-transform: uppercase;
  }

  .event-details {
    position: absolute;
    left: 370px;
    top: 560px;
    right: 70px;
  }
  .venue-name { font-size: 22px; font-weight: 800; text-transform: uppercase; }
  .venue-address { font-size: 18px; font-weight: 500; margin-top: 6px; white-space: nowrap; }

  .reply {
    margin-top: 40px;
    display: flex;
    align-items: baseline;
    gap: 12px;
    font-size: 19px;
    font-weight: 700;
    white-space: nowrap;
  }
  .checkbox {
    display: inline-block;
    width: 20px;
    height: 20px;
    border: 2px solid var(--line);
    flex: none;
    position: relative;
    top: 3px;
  }
  .checkbox.large { width: 28px; height: 28px; border-width: 3px; }
  .reply .yes { font-size: 34px; font-weight: 800; }

  .levels {
    margin-top: 20px;
    display: flex;
    gap: 34px;
    font-size: 18px;
  }
  .level { display: flex; align-items: baseline; gap: 10px; }
  .level b { font-weight: 700; }

  .paid-by {
    margin-top: 26px;
    display: flex;
    align-items: flex-end;
    gap: 10px;
    font-size: 17px;
  }
  .paid-by .blank { flex: 1; border-bottom: 2px solid var(--line); height: 20px; }

  .cheque-address {
    margin-top: 44px;
    font-size: 17px;
    line-height: 1.5;
    color: var(--muted);
  }

  .footer {
    position: absolute;
    left: 330px;
    right: 30px;
    top: 995px;
    color: var(--white);
  }
  .rsvp { font-size: 20px; font-weight: 700; white-space: nowrap; }
  .legal { margin-top: 20px; font-size: 15px; line-height: 1.6; font-weight: 400; opacity: .95; }
</style>
</head>
<body>
  <main class="flyer">
    <h1 class="candidate-first">MARCUS</h1>

    <div class="portrait" role="img" aria-label="Portrait photograph of the candidate in a dark suit"></div>

    <section class="content-panel">
      <div class="panel-inner">
        <div class="candidate-last">WHITFIELD</div>
        <p class="district">Harlow County · District 4</p>
        <p class="invite-line">Cordially invites you to our Annual Fundraiser</p>
      </div>
    </section>

    <div class="date-band">
      <div>Thursday – June 11, 2016</div>
      <div>6:00 – 8:00 PM</div>
    </div>

    <section class="event-details">
      <p class="venue-name">Lantern Hall Gallery</p>
      <p class="venue-address">Crestview Plaza, 4120 Meadow Brook Lane, Glenwood, MD</p>

      <div class="reply">
        <span class="checkbox large"></span>
        <span><span class="yes">Yes!</span> I plan to attend, enclosed is my cheque for</span>
      </div>

      <div class="levels">
        <span class="level"><span class="checkbox"></span><span><b>Bronze:</b> $250</span></span>
        <span class="level"><span class="checkbox"></span><span><b>Silver:</b> $500</span></span>
        <span class="level"><span class="checkbox"></span><span><b>Gold:</b> $1,000</span></span>
      </div>

      <div class="paid-by"><span>Paid for by</span><span class="blank"></span></div>

      <p class="cheque-address">Please make the cheque to: Marcus Whitfield, PO Box 51870,<br>4120 Meadow Brook Lane, Glenwood, MD</p>
    </section>

    <footer class="footer">
      <p class="rsvp">Please RSVP by email: rsvp@whitfieldcampaign.org</p>
      <p class="legal">Pennsylvania law allows personal, partnership, and PAC contributions.<br>By law we cannot accept corporate contributions</p>
    </footer>
  </main>
</body>
</html>
```